Resume for CEO

I need two formats of a resume created.

#1. It is 3 pages long and is the extended version.

#2. Is the 1 page resume.

Both should have the same styling. I am attaching the long and short version in word. I am also attaching a temporary picture for the resume. I will switch that out myself. Don't worry about keeping the sizing. It can be whatever you want.

There is a good website to use as a reference. http://brindlecvs.com/
The reason I am not using this site is because they don't give you the files for editing. They make you use them to edit.

Please feel free to ask questions. I"m excited to see the ideas that come up.

End format should be in AI with PDF's. I want 1 resume that is 3-4 pages and one that is 1 page. They should have the same style.

Dale

Reason: I have only received 2 designs. Hopefully I can get more submissions.

Reason: I need to get the design finalized and I will end the project.

```html
<!DOCTYPE html>
<html lang="en">
<head>
<meta charset="utf-8">
<title>Dale S. Hartwell — Resume</title>
<link href="https://fonts.googleapis.com/css2?family=Oswald:wght@300;400;500&family=Open+Sans:wght@400;600&display=swap" rel="stylesheet">
<style>
  :root{
    --bg:#e4e4e5;
    --paper:#e9e9ea;
    --panel:#f5f5f5;
    --green:#1c3b2b;
    --green-line:#5c7a66;
    --grey-bar:#8b8b8d;
    --grey-border:#b9b9bb;
    --ink:#3a3a3a;
    --white:#ffffff;
  }
  *{margin:0;padding:0;box-sizing:border-box}
  html,body{width:1200px;height:887px;overflow:hidden;background:var(--bg)}
  body{position:relative;font-family:"Open Sans",Arial,sans-serif;color:var(--ink)}
  .resume{position:absolute;left:325px;top:60px;width:550px;height:767px;background:var(--paper);box-shadow:3px 4px 8px rgba(0,0,0,.25)}
  .top-strip{position:absolute;left:357px;top:8px;width:193px;height:25px;background:var(--grey-bar)}
  .summary{position:absolute;left:0;top:9px;width:357px;height:141px;background:var(--green);color:var(--white);padding:7px 12px 0 14px}
  .summary::after{content:"";position:absolute;inset:4px;border:1px dashed rgba(255,255,255,.25);pointer-events:none}
  .summary h2{font-family:"Oswald",sans-serif;font-weight:400;font-size:11.5px;letter-spacing:.3px;margin-bottom:4px}
  .summary p{font-size:7.3px;line-height:10.6px;text-align:justify}
  .photo-frame{position:absolute;left:370px;top:3px;width:171px;height:215px;background:var(--white);border:1px solid var(--green-line);padding:5px}
  .photo{width:100%;height:100%;background:linear-gradient(160deg,#b0651c 0%,#d6953a 45%,#7a4a24 80%,#3d3a3c 100%)}
  .name{position:absolute;left:25px;top:156px;font-family:"Oswald",sans-serif;font-weight:400;font-size:24px;color:var(--green)}
  .contact{position:absolute;left:25px;top:190px;font-family:"Oswald",sans-serif;font-size:8.6px;color:var(--green);line-height:14px}
  .contact span{margin-right:14px}
  .keywords{position:absolute;left:12px;top:230px;width:524px;height:30px;background:var(--grey-bar);color:var(--white);font-family:"Oswald",sans-serif;font-weight:300;font-size:8.4px;line-height:13px;text-align:center;padding-top:2px}
  .section{position:absolute;left:15px;width:520px;background:var(--panel);border:2px solid var(--grey-border);padding:4px}
  .section-inner{border:1px dashed var(--grey-border);height:100%;padding:4px 8px 0 10px}
  .section h3{font-family:"Oswald",sans-serif;font-weight:300;font-size:12.5px;color:#7a7a7a;margin-bottom:8px}
  .role{margin-bottom:9px}
  .role h4{font-family:"Oswald",sans-serif;font-weight:400;font-size:10.5px;color:var(--green)}
  .role .org{font-size:7.3px;color:#555;margin:1px 0 4px}
  .role p{font-size:7.1px;line-height:10.4px;text-align:justify}
  .experience{top:272px;height:165px}
  .ventures{top:448px;height:262px}
  .education{position:absolute;left:0;top:712px;width:550px;height:55px;background:var(--green);color:var(--white);padding:4px}
  .education-inner{border:1px dashed rgba(255,255,255,.25);height:100%;position:relative}
  .education h3{position:absolute;left:21px;top:2px;font-family:"Oswald",sans-serif;font-weight:400;font-size:8.5px}
  .degree{position:absolute;top:12px;text-align:center}
  .degree strong{display:block;font-family:"Oswald",sans-serif;font-weight:500;font-size:9px}
  .degree span{font-size:7px}
  .degree-one{left:87px;width:150px}
  .degree-two{left:245px;width:215px}
</style>
</head>
<body>
<main class="resume">
  <div class="top-strip"></div>

  <section class="summary">
    <h2>CHIEF EXECUTIVE OFFICER &nbsp;•&nbsp; ENTREPRENEUR</h2>
    <p>Dynamic Chief Executive Officer with over 16 years of experience in providing strategic direction and leadership for organizations in multiple markets with unique situations. Extensive experience transforming companies into profitable and progressive organizations using proven systematic implementation. Offers comprehensive knowledge and operational experience with highly-engineered technical manufacturing companies, ecommerce and international brand building. Effectively identifies critical business drivers in multiple markets and industries, enabling growth opportunities within a variety of departments and ultimately complete business expansion.</p>
  </section>

  <div class="photo-frame"><div class="photo" role="img" aria-label="Portrait photo of the candidate"></div></div>

  <h1 class="name">Dale S. Hartwell</h1>
  <div class="contact">
    <div><span>4810 CANYON VISTA RD. STE. 207</span>•&nbsp;&nbsp;&nbsp; SAN DIEGO, CA 92131</div>
    <div><span>T: &nbsp;(619) 555-0184</span><span>E: &nbsp;dalehartwell22@mailbox.com</span></div>
  </div>

  <div class="keywords">CEO &nbsp;• &nbsp;LEADERSHIP&amp; VISION &nbsp;• &nbsp;TURNAROUND &nbsp;• &nbsp;CORPORATE RESTRUCTURING &nbsp;• &nbsp;BRAND BUILDING &nbsp;• &nbsp;PRODUCT DEVELOPMENT<br>&amp; CONTRACT MANUFACTURING &nbsp;• &nbsp;STRONG FINANCIAL ACCOUNTING &nbsp;• &nbsp;SALES&amp; MARKETING STRATEGIC &nbsp;PLANNING</div>

  <section class="section experience">
    <div class="section-inner">
      <h3>PROFESSIONAL EXPERIENCE</h3>
      <div class="role">
        <h4>Interim Chief Executive Officer &nbsp;•&nbsp; August 2013 - January 2014</h4>
        <div class="org">Melted Bread Truck TX, LLC: Austin, TX &nbsp;&nbsp;(www.meltedbreadtruck.com)</div>
        <p>Provides strategic direction as Interim CEO for this innovative gourmet food truck company aiming to be first publicly traded food truck company in the United States.</p>
      </div>
      <div class="role">
        <h4>Chief Executive Officer &nbsp;•&nbsp; May 2009 - November 2011</h4>
        <div class="org">Ashcombe Handcrafted Bicycles, Inc.: San Diego, CA (www.ashcombebikes.com)</div>
        <p>Turned this ailing specialty bicycle company around through rebranding efforts and improved marketing and sales strategy, accelerating to profitable state within 12 months.</p>
      </div>
    </div>
  </section>

  <section class="section ventures">
    <div class="section-inner">
      <h3>ENTREPRENEURIAL EXPERIENCE</h3>
      <div class="role">
        <h4>Co- Founder &amp; Chief Executive Officer &nbsp;•&nbsp; January 2011 - Present</h4>
        <div class="org">Signpost Media, Inc.: San Diego, CA</div>
        <p>Serves as Co-Founder and CEO for this marketing, media, branding, public relation, and corporate consulting company providing valuable resources to public, private, and non-profit sector organizations.</p>
      </div>
      <div class="role">
        <h4>Founder &amp; Chief Executive Officer &nbsp;•&nbsp; May 2009 - Present</h4>
        <div class="org">Torque Precision, Inc.: San Diego, CA (www.TorqueUSA.com)</div>
        <p>Founded this cutting-edge company, redefining the level of technology, quality, and product weight in the bicycle component segment of the cycling industry launching toward international distribution and representation in 23 countries.</p>
      </div>
      <div class="role">
        <h4>Founder &amp; Chief Executive Officer &nbsp;•&nbsp; December 1999 - April 2009</h4>
        <div class="org">Further Afield, Inc.: San Diego, CA</div>
        <p>Further Afield, Inc. experienced explosive revenue growth fueled by strategic purchasing partnerships, aggressive sales and marketing techniques, and new cutting-edge ecommerce technology implementation. &nbsp;&nbsp;Following the development of new verticals, watersports, and camping, Further Afield, Inc. was acquired after becoming one of nation's largest e-commerce, mail-order, brick and mortar specialty retailers. &nbsp;Purchased by Critter Union, Inc. in 2009 by owners of pawsandpedals.com.</p>
      </div>
    </div>
  </section>

  <footer class="education">
    <div class="education-inner">
      <h3>EDUCATION</h3>
      <div class="degree degree-one"><strong>General Studies &amp; Pre-Med</strong><span>Westbluff University</span></div>
      <div class="degree degree-two"><strong>Bachelor of Science in Business Administration/Marketing</strong><span>Coastal Pacific University</span></div>
    </div>
  </footer>
</main>
</body>
</html>
```